Add words, element to an already make product design

Hi guys,
I m already have the design (attached) which is a wet tissue product. The front main side (about 14cm x 7 cm) is the waves and the brand name Zelfo. However, in this main side, it should contain more words, which are "Khan uot" (mean wet wipe), and the words "Mat lanh" (mean cooling) and "Tinh khiet" (mean purity). "Khan uot" to indicate function of the product, while Mat lanh and Tinh khiet are just marketing term to add.
So yes, the task is quite simple, but I think the key is to choose an appropriate font, color and the location you decide where it should be. You can add any element you want, as long as it look good overall, and those words above, are required to have. More in the attached are few rival from our market, as some example.
Thank you, and wait your idea.

Hi guys, Just to tell you that the main front design will not change. So the waves and the brand name still keep the same. Just adding more words or elements to it. Thank you guys.

```html
<!DOCTYPE html>
<html lang="vi">
<head>
<meta charset="utf-8">
<title>Zelfo – khăn ướt, dieline</title>
<link href="https://fonts.googleapis.com/css2?family=Nunito:wght@600;800;900&family=Roboto:wght@400;500&display=swap" rel="stylesheet">
<style>
  :root {
    --ink: #111111;
    --brand-blue: #3f97d1;
    --deep-blue: #2a72bb;
    --sky-blue: #8fcdf0;
    --label-blue: #2f6fb5;
    --paper: #ffffff;
  }
  html, body {
    margin: 0;
    padding: 0;
    width: 1138px;
    height: 1200px;
    overflow: hidden;
    background: var(--paper);
  }
  .canvas {
    position: relative;
    width: 1138px;
    height: 1200px;
    font-family: "Nunito", sans-serif;
  }
  .artwork { position: absolute; left: 0; top: 0; }
  .dim {
    position: absolute;
    font-family: "Roboto", sans-serif;
    color: var(--ink);
    line-height: 1;
    white-space: nowrap;
  }
  .dim--top { font-size: 40px; transform: translateX(-50%); }
  .dim--side { font-size: 30px; transform: translate(-50%, -50%) rotate(90deg); }
  .dim--height { font-size: 40px; transform: translate(-50%, -50%) rotate(-90deg); }
  .dim--width { font-size: 46px; transform: translateX(-50%); }

  .brand-name {
    position: absolute;
    left: 556px;
    top: 548px;
    transform: translateX(-50%) rotate(-4deg);
    font-size: 150px;
    font-weight: 900;
    color: var(--brand-blue);
    letter-spacing: -2px;
    line-height: 1;
  }
  .function-tag {
    position: absolute;
    left: 452px;
    top: 655px;
    width: 226px;
    height: 56px;
    border-radius: 30px 30px 30px 4px;
    background: var(--deep-blue);
    color: var(--paper);
    font-size: 30px;
    font-weight: 800;
    display: flex;
    align-items: center;
    justify-content: center;
    transform: rotate(4deg);
    letter-spacing: 1px;
  }
  .claim {
    position: absolute;
    font-size: 16px;
    font-weight: 800;
    color: var(--label-blue);
    transform: translateX(-50%);
  }
  .claim-dot {
    position: absolute;
    border-radius: 50%;
  }
  .claim-dot--cool { left: 783px; top: 394px; width: 72px; height: 72px; background: var(--brand-blue); }
  .claim-dot--pure { left: 884px; top: 399px; width: 70px; height: 70px; background: var(--sky-blue); }

  .expiry-note {
    position: absolute;
    left: 408px;
    top: 193px;
    font-family: "Roboto", sans-serif;
    font-size: 12px;
    color: var(--label-blue);
    line-height: 15px;
  }
  .disposal-note {
    position: absolute;
    left: 202px;
    top: 232px;
    width: 80px;
    font-family: "Roboto", sans-serif;
    font-size: 9px;
    font-weight: 500;
    color: var(--label-blue);
    text-align: center;
    line-height: 12px;
    transform: rotate(180deg);
  }
  .batch-mark {
    position: absolute;
    left: 40px;
    top: 1051px;
    width: 32px;
    height: 64px;
    background: var(--brand-blue);
  }
  .batch-mark span {
    position: absolute;
    left: 2px;
    top: 4px;
    font-family: "Roboto", sans-serif;
    font-size: 13px;
    color: var(--ink);
    transform: rotate(90deg);
    transform-origin: 8px 8px;
  }
  .print-window {
    position: absolute;
    left: 703px;
    top: 863px;
    width: 244px;
    height: 97px;
    background: var(--paper);
  }
</style>
</head>
<body>
<div class="canvas">
  <svg class="artwork" width="1138" height="1200" viewBox="0 0 1138 1200">
    <defs>
      <linearGradient id="waterWash" x1="0" y1="0" x2="0" y2="1">
        <stop offset="0" stop-color="#e4f2fb"/>
        <stop offset="0.25" stop-color="#8ec8ec"/>
        <stop offset="0.5" stop-color="#3e9bd8"/>
        <stop offset="1" stop-color="#2b78c3"/>
      </linearGradient>
    </defs>

    <path role="img" aria-label="Watercolour waves in layered blues across the front and bottom panels"
          d="M125 505 C 240 560, 360 640, 520 680 C 660 710, 760 560, 985 565 L 985 1047 L 120 1047 L 120 510 Z"
          fill="url(#waterWash)"/>

    <g class="pictograms" fill="#e3f1fa" stroke="var(--label-blue)" stroke-width="2">
      <rect role="img" aria-label="Usage pictogram" x="291" y="227" width="36" height="36" rx="5"/>
      <rect role="img" aria-label="Usage pictogram" x="337" y="227" width="36" height="36" rx="5"/>
      <rect role="img" aria-label="Usage pictogram" x="383" y="227" width="36" height="36" rx="5"/>
      <rect role="img" aria-label="Usage pictogram" x="291" y="272" width="36" height="36" rx="5"/>
      <rect role="img" aria-label="Usage pictogram" x="337" y="272" width="36" height="36" rx="5"/>
      <rect role="img" aria-label="Usage pictogram" x="383" y="272" width="36" height="36" rx="5"/>
      <rect role="img" aria-label="Dispose in bin pictogram" x="223" y="266" width="36" height="36" rx="5"/>
    </g>

    <path class="cert-badge" role="img" aria-label="Certification badge"
          d="M818 222 L 916 222 L 922 300 Q 867 320 812 300 Z" fill="var(--deep-blue)"/>

    <g class="dieline" fill="none" stroke="var(--ink)" stroke-width="2" stroke-dasharray="22 12">
      <rect x="40" y="57" width="1025" height="1071"/>
      <line x1="120" y1="57" x2="120" y2="1128"/>
      <line x1="985" y1="57" x2="985" y2="1128"/>
      <line x1="40" y1="137" x2="1065" y2="137"/>
      <line x1="40" y1="365" x2="1065" y2="365"/>
      <line x1="40" y1="820" x2="1065" y2="820"/>
      <line x1="40" y1="1047" x2="1065" y2="1047"/>
    </g>
  </svg>

  <div class="dim dim--top" style="left:88px; top:10px;">12.5</div>
  <div class="dim dim--top" style="left:551px; top:6px;">135</div>
  <div class="dim dim--top" style="left:1025px; top:10px;">12.5</div>
  <div class="dim dim--side" style="left:1100px; top:97px;">12.5</div>
  <div class="dim dim--side" style="left:1100px; top:220px;">35</div>
  <div class="dim dim--side" style="left:1100px; top:560px;">70</div>
  <div class="dim dim--side" style="left:1100px; top:905px;">35</div>
  <div class="dim dim--side" style="left:1100px; top:1113px;">12.5</div>
  <div class="dim dim--height" style="left:18px; top:597px;">165mm</div>
  <div class="dim dim--width" style="left:549px; top:1148px;">160 mm</div>

  <div class="expiry-note">NSX: 2 năm trước HSD<br>HSD: In trên bao bì</div>
  <div class="disposal-note">XIN BỎ VÀO ĐÚNG<br>NƠI QUY ĐỊNH</div>

  <div class="claim-dot claim-dot--cool"></div>
  <div class="claim-dot claim-dot--pure"></div>
  <div class="claim" style="left:816px; top:472px;">Matlanh</div>
  <div class="claim" style="left:914px; top:472px;">Tinhkhiet</div>

  <div class="brand-name">Zelfo</div>
  <div class="function-tag">khanuot</div>

  <div class="print-window"></div>
  <div class="batch-mark"><span>BH</span></div>
</div>
</body>
</html>
```